New locally owned rental company needs a flyer to circulate

Need flyer with logo, phone# and address. We rent cars to anyone with driver's license and proper insurance. Rates as low as $50/day. Can offer compact cars, mid-size and full size sedans. Also SUV's.

```html
<!DOCTYPE html>
<html lang="en">
<head>
<meta charset="utf-8">
<title>DriveSoon – Rent a Car Flyer</title>
<link href="https://fonts.googleapis.com/css2?family=Montserrat:wght@400;500;600;700;800;900&display=swap" rel="stylesheet">
<style>
  :root {
    --green: #27a24c;
    --green-soft: #8fcb93;
    --green-pale: #dcefdc;
    --blue: #1150a0;
    --ink: #111111;
    --paper: #eeeeee;
    --stage: #e4e4e4;
    --white: #ffffff;
  }
  * { box-sizing: border-box; margin: 0; padding: 0; }
  html, body {
    width: 1200px; height: 768px; overflow: hidden;
    background: var(--stage);
    font-family: "Montserrat", Arial, sans-serif;
  }
  .flyer {
    position: absolute; left: 88px; top: 0;
    width: 1024px; height: 768px; overflow: hidden;
    background: var(--paper);
  }
  .flyer__sky {
    position: absolute; left: 0; top: 0; width: 100%; height: 420px;
    background: linear-gradient(180deg, #f4f7f4 0%, var(--green-pale) 35%, var(--green-soft) 100%);
  }
  .flyer__shapes { position: absolute; inset: 0; }
  .headline {
    position: absolute; left: 70px; top: 58px;
    color: var(--green); font-weight: 800; font-size: 82px; letter-spacing: 1px; line-height: 1;
  }
  .headline__rule {
    position: absolute; left: 70px; top: 150px; width: 548px; height: 7px; background: var(--green);
  }
  .intro {
    position: absolute; left: 72px; top: 176px;
    color: var(--ink); font-weight: 500; font-size: 25px; line-height: 1.25;
  }
  .car-photo {
    position: absolute; left: 380px; top: 225px; width: 610px; height: 285px;
    border-radius: 150px 110px 40px 60px;
    background: radial-gradient(ellipse at 55% 55%, #b3222b 0%, #8e1820 55%, #5a1216 100%);
  }
  .rate-badge { position: absolute; left: 96px; top: 262px; width: 280px; height: 280px; }
  .brand { position: absolute; left: 72px; top: 548px; }
  .brand__name {
    color: var(--blue); font-weight: 900; font-size: 56px; line-height: 1;
  }
  .brand__tagline {
    margin-top: 8px; color: var(--ink); font-weight: 700; font-size: 21px; letter-spacing: 6px; line-height: 1;
  }
  .notice {
    position: absolute; left: 10px; top: 664px; width: 520px;
    color: var(--white); font-weight: 500; font-size: 19px; line-height: 1.3; text-align: center;
  }
  .book-now {
    position: absolute; left: 720px; top: 520px; width: 270px; height: 62px;
    border-radius: 31px; background: var(--blue);
    color: var(--white); font-weight: 700; font-size: 32px; letter-spacing: 1px;
    display: flex; align-items: center; justify-content: center;
  }
  .contact-phone {
    position: absolute; right: 36px; top: 590px; height: 60px;
    display: flex; align-items: center; gap: 20px;
    color: var(--ink); font-weight: 600; font-size: 38px; white-space: nowrap;
  }
  .contact-address {
    position: absolute; right: 36px; top: 662px;
    display: flex; align-items: center; gap: 24px;
  }
  .contact-address__text {
    color: var(--ink); font-weight: 500; font-size: 19px; line-height: 1.3;
    text-align: right; white-space: nowrap;
  }
</style>
</head>
<body>
  <main class="flyer">
    <div class="flyer__sky"></div>

    <svg class="flyer__shapes" width="1024" height="768" viewBox="0 0 1024 768" aria-hidden="true">
      <polygon class="stripe-green" points="700,0 820,0 720,260 600,260" fill="var(--green)"/>
      <polygon class="stripe-blue" points="820,0 900,0 800,260 720,260" fill="var(--blue)"/>
      <polygon class="phone-band" points="569,590 1024,590 1024,650 552,650" fill="var(--green)"/>
      <polygon class="notice-band" points="0,652 551,652 530,732 0,732" fill="var(--blue)"/>
      <line class="divider" x1="600" y1="480" x2="520" y2="768" stroke="var(--green)" stroke-width="3"/>
      <rect class="base-strip" x="0" y="748" width="1024" height="20" fill="var(--green)"/>
    </svg>

    <h1 class="headline">RENT A CAR</h1>
    <div class="headline__rule"></div>
    <p class="intro">We offer compact cars, mid-size,<br>full size sedans and SUV's.</p>

    <div class="car-photo" role="img" aria-label="Photo of a red mid-size sedan with a rental sign on the windshield"></div>

    <svg class="rate-badge" viewBox="0 0 280 280" role="img" aria-label="Rates as low as $50 per day">
      <defs>
        <path id="badge-arc" d="M30,140 A110,110 0 0 1 250,140"/>
      </defs>
      <circle cx="140" cy="140" r="138" fill="var(--green)"/>
      <path d="M34,150 A106,106 0 0 0 246,150" fill="none" stroke="var(--white)" stroke-width="2"/>
      <text font-family="Montserrat, Arial, sans-serif" font-size="26" font-weight="500" fill="var(--white)" letter-spacing="1">
        <textPath href="#badge-arc" startOffset="50%" text-anchor="middle">Rates as low as</textPath>
      </text>
      <polygon points="112,84 166,82 146,118" fill="var(--white)"/>
      <text x="140" y="180" text-anchor="middle" font-family="Montserrat, Arial, sans-serif" font-size="62" font-weight="800" fill="var(--ink)">$50</text>
      <text x="146" y="216" text-anchor="middle" font-family="Montserrat, Arial, sans-serif" font-size="26" font-weight="600" fill="var(--ink)">Per day</text>
    </svg>

    <div class="brand">
      <div class="brand__name">DriveSoon</div>
      <div class="brand__tagline">Car &amp; Van Rental</div>
    </div>

    <p class="notice">We rent cars to anyone with driver's<br>license and proper insurance</p>

    <div class="book-now">BOOK NOW!</div>

    <div class="contact-phone">
      <svg width="32" height="32" viewBox="0 0 24 24" aria-hidden="true">
        <path d="M6.6 10.8a15 15 0 0 0 6.6 6.6l2.2-2.2a1 1 0 0 1 1-.25 11.4 11.4 0 0 0 3.6.57 1 1 0 0 1 1 1V20a1 1 0 0 1-1 1A17 17 0 0 1 3 4a1 1 0 0 1 1-1h3.5a1 1 0 0 1 1 1c0 1.25.2 2.45.57 3.57a1 1 0 0 1-.25 1z" fill="var(--white)"/>
      </svg>
      <span>555-014-2290</span>
    </div>

    <div class="contact-address">
      <svg width="26" height="35" viewBox="0 0 24 32" aria-hidden="true">
        <path d="M12 0C5.4 0 0 5.3 0 11.8 0 20.6 12 32 12 32s12-11.4 12-20.2C24 5.3 18.6 0 12 0z" fill="var(--green)"/>
        <circle cx="12" cy="11.5" r="4.5" fill="var(--paper)"/>
      </svg>
      <p class="contact-address__text">4870B South Harbor<br>Avenue Riverton,<br>AL 35990</p>
    </div>
  </main>
</body>
</html>
```